Zielgruppe
Wir beraten Menschen aus unterschiedlichen Branchen, die im Rahmen Ihrer Tätigkeit vor einem technologischen Problem bzw. einer technologischen Lücke stehen und helfen diesen über vielfältige Bausteine, um so dem Unternehmen ein Unternehmensupgrade zu verschaffen. Wir schlagen somit eine Brücke zwischen dem Stand von heute in einem Unternehmen zu einem besseren Stand morgen.
Konkret betreiben wir unter anderem externes Projektmanagement, beschaffen Informationen unterschiedlicher Art, vermitteln Kooperationspartner, beraten individuell uvm.
Ob jemand nach einer neuen, innovativen Technologie sucht, Partner benötigt, um eigene Neuentwicklungen voranzutreiben, ein neues Produkt fürs eigene Unternehmen und einen entsprechenden Prototypen sucht, verwendete Stoffe mit anderen ersetzen will - mithilfe unseres weltweiten Expertennetzwerks von über 600.000 direkten Ansprechpartnern finden wir für die meisten Nöte dieser Art eine Lösung bzw. jemanden, der diese lösen kann.
Im Grunde genommen beseitigen wir Engpässe innerhalb von Industrieunternehmen, die beispielsweise sein können
-fehlende TEchnologien/Ersatzprodukte/Ersatzstoffe
-fehlende Ideen für Neuentwicklungen
-fehlendes Wissen im Unternehmen
-fehlende Objektivität hinsichtlich interner Verbesserungsmöglichkeiten
-fehlende Zeit für eigene Projekte, Neuentwicklungen und Suchen versch. Art
Wir finden
- neue Technologien, Ersatzprodukte, Ersatzstoffe
- Ideen für Neuentwicklungen und zusätzlich diejenigen, die dabei unterstützen können
- neue Märkte, um das Unternehmen zu erweitern
- das fehlende Wissen
- den nötigen Abstand, um interne Prozesse und Abläufe objektiv zu beurteilen und geben Vorschläge zur Veränderung/Verbesserung
- passende Realisierungspartner
Wie?
- wir recherchieren (Patente, Literatur) und sammeln Hintergrundwissen
- wir befragen unser Netzwerk und Unternehmen/Wissenschaftler
- wir setzen unsere Töchter..
Aufgabenstellung
Wir benötigen einen faltbaren Flyer, allerdings keinen klassischen, sondern wie ein Theatervorhang. Beispielbilder sind anbei (wir würden die Flyer drucken lassen und dann selbst falten). Wir gehen gerne andere Wege, auch in unseren Projekten.
Der Mensch und dessen Wünsche soll im Mittelpunkt stehen.
Design sollte nicht zu verspielt sein, sich daran orientieren, dass deutsche Unternehmen damit angesprochen werden.
Einen Beispielflyer mit den (noch variablen) Texten ist beigefügt, das Design muss sich nicht daran orientieren. Gute Alternativen sind mehr als gewünscht.
Der Gedanke hinter dem Flyer: Wir schlagen eine Brücke für den Kunden/Menschen zu seinem Ziel. Die Tools, die wir dazu nutzen sind Steine oder wir sprengen den Weg frei zum Ziel o.ä. Auch hier sind Alternativen mehr als willkommen.
Sie dürfen sich so weit wie möglich vom Beispielentwurf und dem Bild der Brücke zum Ziel lösen. Je kreativer und einleuchtender, desto besser. Gerne auch humorvoll, gerne einfach anders.

```html
<!DOCTYPE html>
<html lang="de">
<head>
<meta charset="utf-8">
<title>Brückwerk – Gatefold-Flyer</title>
<link rel="stylesheet" href="https://fonts.googleapis.com/css2?family=Lato:ital,wght@0,300;0,400;0,700;0,900;1,300;1,700&display=swap">
<style>
:root{
  --navy:#262f86;
  --navy-band:rgba(38,47,134,.86);
  --sky-top:#2f64b4;
  --sky-mid:#6f93c6;
  --dusk:#c9cfdd;
  --water:#8d9bb3;
  --steel:#2a2f3d;
  --paper:#f4f5f8;
  --stage:#e9eaee;
  --ink-grey:#6b6f7c;
  --white:#ffffff;
}
*{box-sizing:border-box;margin:0;padding:0}
html,body{width:1200px;height:984px;overflow:hidden}
body{background:var(--stage);font-family:"Lato",sans-serif;position:relative}

.sheet{position:absolute;display:flex;box-shadow:0 6px 18px rgba(30,35,60,.18)}
.sheet--cover{left:330px;top:32px;width:540px;height:440px}
.sheet--inside{left:60px;top:512px;width:1080px;height:440px}

.panel{position:relative;height:100%;overflow:hidden}
.panel + .panel{border-left:1px solid rgba(255,255,255,.35)}

.photo{position:absolute;inset:0;
  background:linear-gradient(180deg,var(--sky-top) 0%,var(--sky-mid) 45%,var(--dusk) 62%,var(--steel) 64%,var(--steel) 68%,var(--water) 70%,#b7c0d0 100%)}
.photo--faded{opacity:.22}

/* cover */
.cover-panel{width:270px}
.band{position:absolute;background:var(--navy-band);color:var(--white)}
.band--left{left:34px;top:40px;width:200px;height:370px;padding:18px 16px}
.band--right{left:70px;top:186px;width:180px;height:234px;padding:16px 14px}
.cover-question{font-weight:300;font-size:19px;line-height:1.12}
.cover-answer{font-weight:900;font-size:19px;margin:6px 0 8px}
.cover-intro{font-size:10.5px;font-weight:300;margin-bottom:6px}
.cover-intro b{font-weight:900;font-style:italic}
.checklist{list-style:none}
.checklist li{display:flex;gap:7px;font-size:10px;font-weight:300;line-height:1.15;margin-bottom:5px}
.checklist svg{flex:none;margin-top:2px}
.partner-claim{font-weight:300;font-size:17.5px;line-height:1.2}
.partner-claim b{font-weight:900}

/* inside */
.flap{width:270px;background:var(--paper)}
.center{width:540px;background:var(--paper)}
.flap-note{position:absolute;left:24px;bottom:40px;width:200px;color:var(--navy);font-size:14px;font-weight:300;line-height:1.3}
.flap-note b{font-weight:700}

.tools-head{position:absolute;left:0;top:28px;width:420px;background:var(--navy);color:var(--white);padding:12px 20px;font-size:14px;font-weight:300;line-height:1.3}
.tools-head b{font-weight:900;font-size:16px}
.tools{position:absolute;left:40px;top:118px;width:440px;list-style:none;border-left:1px solid var(--navy);margin-left:40px}
.tools li{position:relative;padding:0 0 14px 18px;font-size:11px;font-weight:300;color:var(--navy);line-height:1.25}
.tools li b{font-weight:700}
.tools svg{position:absolute;left:-62px;top:0}
.upgrade{position:absolute;left:40px;bottom:30px;color:var(--navy);font-size:22px;font-weight:300;line-height:1.2}
.upgrade b{font-weight:900}

.brand{position:absolute;top:22px;left:24px;display:flex;align-items:center;gap:8px;color:var(--navy);font-weight:700;font-size:16px}
.brand-dot{width:14px;height:14px;border-radius:50%;background:var(--navy)}
.vband{position:absolute;left:24px;top:60px;width:22px;height:360px;background:var(--navy)}
.solve{position:absolute;left:62px;top:70px;width:180px;color:var(--navy);font-size:17px;font-weight:300;line-height:1.25}
.solve b{font-weight:700;font-style:italic}
.figure{position:absolute;left:80px;bottom:40px;width:160px;height:150px;border-radius:6px;
  background:linear-gradient(135deg,#3340a6 0%,#6b6f7c 100%);opacity:.85}
</style>
</head>
<body>

<section class="sheet sheet--cover" aria-label="Außenseite">
  <div class="panel cover-panel">
    <div class="photo" role="img" aria-label="Foto einer Hängebrücke über ruhigem Wasser in der Dämmerung"></div>
    <div class="band band--left">
      <p class="cover-question">Sie stehen vor einem technologischen Problem?</p>
      <p class="cover-answer">Keine Sorge.</p>
      <p class="cover-intro"><b>Brückwerk</b> bietet mir:</p>
      <ul class="checklist">
        <li><svg width="9" height="8" viewBox="0 0 9 8"><path d="M1 4l2.5 2.5L8 1" fill="none" stroke="#fff" stroke-width="1.8"/></svg>…neue Technologien, Ersatzprodukte/ Ersatzstoffe</li>
        <li><svg width="9" height="8" viewBox="0 0 9 8"><path d="M1 4l2.5 2.5L8 1" fill="none" stroke="#fff" stroke-width="1.8"/></svg>…Ideen für Neuentwicklungen</li>
        <li><svg width="9" height="8" viewBox="0 0 9 8"><path d="M1 4l2.5 2.5L8 1" fill="none" stroke="#fff" stroke-width="1.8"/></svg>…Zugang zu neuen Märkten</li>
        <li><svg width="9" height="8" viewBox="0 0 9 8"><path d="M1 4l2.5 2.5L8 1" fill="none" stroke="#fff" stroke-width="1.8"/></svg>…ergänzendes Wissen</li>
        <li><svg width="9" height="8" viewBox="0 0 9 8"><path d="M1 4l2.5 2.5L8 1" fill="none" stroke="#fff" stroke-width="1.8"/></svg>…interne Prozess- und Ablaufverbesserungen</li>
        <li><svg width="9" height="8" viewBox="0 0 9 8"><path d="M1 4l2.5 2.5L8 1" fill="none" stroke="#fff" stroke-width="1.8"/></svg>…passende Partner zur Realisierung</li>
        <li><svg width="9" height="8" viewBox="0 0 9 8"><path d="M1 4l2.5 2.5L8 1" fill="none" stroke="#fff" stroke-width="1.8"/></svg>…ein Expertennetzwerk von über 600.000 Ansprechpartnern</li>
      </ul>
    </div>
  </div>
  <div class="panel cover-panel">
    <div class="photo" role="img" aria-label="Fortsetzung des Brückenfotos: Fahrbahn und Wasserfläche"></div>
    <div class="band band--right">
      <p class="partner-claim">Wir beseitigen Ihre <b>Engpässe</b> und sind Ihnen ein strategischer <b>Partner</b> von Beginn bis zum Ende Ihres Projekts.</p>
    </div>
  </div>
</section>

<section class="sheet sheet--inside" aria-label="Innenseite">
  <div class="panel flap">
    <div class="photo photo--faded" role="img" aria-label="Blasses Brückenfoto im Hintergrund"></div>
    <p class="flap-note">Ihr Partner in <b>jedem</b> Projektschritt.</p>
  </div>
  <div class="panel center">
    <div class="photo photo--faded" role="img" aria-label="Blasses Brückenfoto im Hintergrund"></div>
    <p class="tools-head">Wir übernehmen die <b>Gesamtprojektleitung</b>, unternehmen und nutzen für Ihr Projekt passende Tools:</p>
    <ul class="tools">
      <li><svg width="24" height="18" viewBox="0 0 24 18"><rect x="1" y="1" width="22" height="16" rx="2" fill="#3a3d48"/><path d="M5 6h5M5 10h5M14 6h5M14 10h5" stroke="#fff" stroke-width="1.5"/></svg><b>Patent- und Literatur</b>recherchen</li>
      <li><svg width="24" height="18" viewBox="0 0 24 18"><rect x="2" y="2" width="20" height="11" fill="#3a3d48"/><path d="M12 13v4M8 17h8" stroke="#3a3d48" stroke-width="1.5"/></svg>Geographisch spezifische Projektausschreibungen und <b>Netzwerkbefragungen</b></li>
      <li><svg width="24" height="18" viewBox="0 0 24 18"><circle cx="12" cy="8" r="6" fill="#3a3d48"/><rect x="9" y="14" width="6" height="3" fill="#3a3d48"/></svg>Individuelles <b>Projektmanagement</b></li>
      <li><svg width="24" height="18" viewBox="0 0 24 18"><rect x="4" y="1" width="16" height="16" rx="2" fill="#3a3d48"/><path d="M8 7l2 2 4-4M8 13h8" stroke="#fff" stroke-width="1.5" fill="none"/></svg>Tests, Sprint, <b>Validierung</b></li>
      <li><svg width="24" height="18" viewBox="0 0 24 18"><rect x="4" y="1" width="16" height="16" rx="2" fill="#3a3d48"/><path d="M8 13V9M12 13V6M16 13V10" stroke="#fff" stroke-width="1.8"/></svg>Professionelle <b>Marktanalyse</b> und Technologieauswertung</li>
    </ul>
    <p class="upgrade"><b>Unternehmensupgrade</b> durch<br>technologische Beratung</p>
  </div>
  <div class="panel flap">
    <div class="brand"><span class="brand-dot"></span>Brückwerk</div>
    <div class="vband"></div>
    <p class="solve">Wir <b>lösen</b> Ihre unternehmerischen <b>Probleme</b> durch unser Wissen und unsere Tools.</p>
    <div class="figure" role="img" aria-label="Illustration eines Schwarms stilisierter Fische in Blau und Grau"></div>
  </div>
</section>

</body>
</html>
```